Tech business card design

We need an amazing business card design for our new business 'Brakka' a marketing tech startup based in Sydney, Australia. We provide an online marketplace for businesses to search and buy advertising media, connect with service providers and learn more about marketing. We wish to communicate 'cool tech', reliability and professionalism and design based around our logo.

Target Market(s)

Business Owners

Contact Information for Business Card

Name
Position
Email Address
Website
Phone Number

Font styles to use
Other font styles liked:
• Avenir & Avenir Next

Colors

Designer to choose colors to be used in the design.

```html
<!DOCTYPE html>
<html lang="en">
<head>
<meta charset="utf-8">
<title>Brakka Business Card</title>
<link href="https://fonts.googleapis.com/css2?family=Nunito+Sans:wght@300;400;700;900&display=swap" rel="stylesheet">
<style>
  :root {
    --navy: #1b1c58;
    --navy-deep: #0e0f3d;
    --paper: #ffffff;
    --ink-grey: #7a7a84;
    --rule: #3a3a44;
    --backdrop: #2b2b2e;
  }
  * { margin: 0; padding: 0; box-sizing: border-box; }
  html, body { width: 1200px; height: 892px; overflow: hidden; }
  body {
    background: var(--backdrop);
    font-family: "Nunito Sans", sans-serif;
    position: relative;
  }
  .card {
    position: absolute;
    width: 540px;
    height: 330px;
    border-radius: 3px;
    overflow: hidden;
    box-shadow: 0 14px 30px rgba(0,0,0,0.45);
  }
  /* front */
  .card-front {
    left: 170px; top: 80px;
    background: radial-gradient(ellipse at 35% 25%, #26287a 0%, var(--navy) 45%, var(--navy-deep) 100%);
    display: flex; flex-direction: column; align-items: center; justify-content: center;
  }
  .brand-name {
    font-weight: 900;
    letter-spacing: -1px;
    line-height: 1;
  }
  .card-front .brand-name { color: var(--paper); font-size: 92px; }
  .card-front .site {
    margin-top: 34px;
    color: var(--paper);
    font-size: 13px;
    font-weight: 300;
    letter-spacing: 6px;
  }
  /* back */
  .card-back {
    left: 490px; top: 480px;
    background: var(--paper);
  }
  .card-back .brand-name {
    position: absolute; right: 52px; top: 40px;
    color: var(--navy); font-size: 66px;
  }
  .card-back .top-rule {
    position: absolute; left: 215px; right: 18px; top: 196px;
    height: 1px; background: var(--rule);
  }
  .edge-tab {
    position: absolute; left: 0; top: 216px;
    width: 12px; height: 36px; background: var(--navy);
  }
  .person { position: absolute; left: 38px; top: 206px; }
  .person-name { color: var(--navy); font-weight: 700; font-size: 22px; line-height: 1.05; }
  .person-role { color: var(--ink-grey); font-weight: 400; font-size: 17px; line-height: 1.1; }
  .person-rule { width: 215px; height: 1px; background: var(--rule); margin: 10px 0 8px; }
  .contact-line {
    display: flex; align-items: center; gap: 10px;
    color: var(--ink-grey); font-size: 15px; line-height: 1.45;
  }
  .contact-line svg { width: 14px; height: 14px; flex: none; }
  .site-band { position: absolute; right: 0; bottom: 0; width: 230px; height: 62px; }
  .site-band svg { position: absolute; inset: 0; }
  .site-band .site {
    position: absolute; right: 16px; bottom: 20px;
    color: var(--paper); font-size: 14px; letter-spacing: 0.6px;
  }
</style>
</head>
<body>
  <section class="card card-front" aria-label="Card front">
    <div class="brand-name">Brakka</div>
    <div class="site">www.brakkamedia.com.au</div>
  </section>

  <section class="card card-back" aria-label="Card back">
    <div class="brand-name">Brakka</div>
    <div class="top-rule"></div>
    <div class="edge-tab"></div>
    <div class="person">
      <div class="person-name">DANIEL MOORE</div>
      <div class="person-role">FOUNDER, DIRECTOR</div>
      <div class="person-rule"></div>
      <div class="contact-line">
        <svg viewBox="0 0 14 14" aria-hidden="true"><rect x="3" y="0.8" width="8" height="12.4" rx="1.2" fill="none" stroke="#1b1c58" stroke-width="1.5"/><line x1="5.5" y1="11" x2="8.5" y2="11" stroke="#1b1c58" stroke-width="1.2"/></svg>
        <span>+61 (0)412 555 208</span>
      </div>
      <div class="contact-line">
        <svg viewBox="0 0 14 14" aria-hidden="true"><rect x="0.5" y="3" width="13" height="9" fill="#1b1c58"/><polyline points="0.5,3 7,8 13.5,3" fill="none" stroke="#ffffff" stroke-width="1.1"/></svg>
        <span>daniel@brakkamedia.com.au</span>
      </div>
    </div>
    <div class="site-band">
      <svg viewBox="0 0 230 62" preserveAspectRatio="none" aria-hidden="true"><polygon points="14,0 230,0 230,62 0,62" fill="#1b1c58"/></svg>
      <span class="site">www.brakkamedia.com.au</span>
    </div>
  </section>
</body>
</html>
```